Business Card for Coach - ready to print

Design Business Card ready to order prints www.lukasbrenner.coach

* An Overview / Background of the Business & Services
· Coaching
· Personal growth
* The Target Market / Audience you are trying to reach
· private person in different roles (self, familiy, business role)s
* Design Specifics; any preferences or ideas for Style, Colour, Imagery, etc
· See www.lukasbrenner.coach
· "simple" design
· (small) element of surprise / unusual element

* Information that will be placed in the Business Card
· Beratung und Coaching
· Address: Lukas Brenner, Talmatt 42, CH-8531 Winterthur, Mobile +41 76 254 63 07
* Do you have an existing website or Facebook page where designers can learn more about your company?
· lukasbrenner.coach

Target Market(s)

private person in different roles (self, familiy, business role)

Industry/Entity Type

Life Coaching

Contact Information for Business Card

Lukas Brenner
Talmatt 42
CH-8531 Winterthur

Mobile: +41 76 254 63 07
Email: lubr@sonnwelt.ch
www.lukasbrenner.coach

Font styles to use
Sans Serif

Colors

Designer to choose colors to be used in the design.

Requirements
Must have
• "simple" design
• element of surprise / unusual element
• Beratung & Coaching
• see www.lukasbrenner.coach for colors and so...
Nice to have
• TA Symbol (three rings on top of each other) - unsual presentation
• QR Code of Website (see if it fits in and still looks good).

```html
<!DOCTYPE html>
<html lang="de">
<head>
<meta charset="utf-8">
<title>Lukas Brenner – Visitenkarte</title>
<link href="https://fonts.googleapis.com/css2?family=Montserrat:wght@400;500;700&display=swap" rel="stylesheet">
<style>
  :root {
    --page-bg: #d9dadb;
    --card-dark: #48494b;
    --card-light-top: #ffffff;
    --card-light-bottom: #ededee;
    --brand-red: #c4161c;
    --text-grey: #505153;
    --text-white: #ffffff;
    --icon-orange: #f39200;
    --mark-tone: #2f3032;
    --ring: #e6e7e8;
  }
  * { box-sizing: border-box; margin: 0; padding: 0; }
  html, body { width: 1200px; height: 1021px; overflow: hidden; }
  body {
    background: var(--page-bg);
    font-family: "Montserrat", Arial, sans-serif;
    position: relative;
  }
  .card {
    position: absolute;
    left: 220px;
    width: 760px;
    height: 434px;
    overflow: hidden;
    box-shadow: 0 10px 28px rgba(0,0,0,0.25);
  }
  .card--back { top: 60px; background: var(--card-dark); display: flex; align-items: center; justify-content: center; }
  .card--front { top: 527px; background: linear-gradient(180deg, var(--card-light-top), var(--card-light-bottom)); }

  .back-name {
    color: var(--mark-tone);
    font-weight: 700;
    font-size: 38px;
    letter-spacing: 1px;
  }

  .dark-band { position: absolute; background: var(--card-dark); }
  .dark-band--left { left: 0; top: 168px; width: 232px; height: 266px; }
  .dark-band--right { left: 0; top: 272px; width: 760px; height: 162px; }

  .portrait {
    position: absolute;
    left: 143px; top: 112px;
    width: 176px; height: 176px;
    border-radius: 50%;
    border: 7px solid #fff;
    box-shadow: 0 0 0 2px var(--ring);
    background: radial-gradient(circle at 50% 38%, #b5a08e 0 22%, transparent 23%),
                linear-gradient(180deg, #9fa3a7 0%, #8c9095 55%, #6f7f96 78%, #3f4248 100%);
  }

  .identity { position: absolute; left: 470px; top: 176px; }
  .identity__name {
    color: var(--brand-red);
    font-weight: 700;
    font-size: 25px;
    letter-spacing: 1.5px;
    text-transform: uppercase;
  }
  .identity__role {
    color: var(--text-grey);
    font-size: 19px;
    margin-top: 2px;
  }

  .contact {
    position: absolute;
    left: 450px; top: 298px;
    color: var(--text-white);
    font-size: 18px;
    line-height: 24px;
  }
  .contact__address { margin-bottom: 8px; padding-left: 2px; }
  .contact__row { display: flex; align-items: center; gap: 8px; }
  .contact__icon { width: 18px; height: 18px; flex: none; }
</style>
</head>
<body>

  <section class="card card--back" aria-label="Rückseite">
    <span class="back-name">Lukas Brenner</span>
  </section>

  <section class="card card--front" aria-label="Vorderseite">
    <div class="dark-band dark-band--left"></div>
    <div class="dark-band dark-band--right"></div>

    <div class="portrait" role="img" aria-label="Porträtfoto von Lukas Brenner"></div>

    <div class="identity">
      <div class="identity__name">Lukas Brenner</div>
      <div class="identity__role">Beratung &amp; Coaching</div>
    </div>

    <div class="contact">
      <div class="contact__address">Talmatt 42<br>CH-8531 Winterthur</div>
      <div class="contact__row">
        <svg class="contact__icon" viewBox="0 0 18 18" fill="none" stroke="var(--icon-orange)" stroke-width="1.6">
          <rect x="5" y="1.5" width="8" height="15" rx="1.5"/><line x1="8" y1="14" x2="10" y2="14"/>
        </svg>
        <span>+41 76 254 63 07</span>
      </div>
      <div class="contact__row">
        <svg class="contact__icon" viewBox="0 0 18 18" fill="none" stroke="var(--icon-orange)" stroke-width="1.6">
          <rect x="1.5" y="4" width="15" height="10" rx="1"/><polyline points="1.5,4 9,10 16.5,4"/>
        </svg>
        <span>lubr@sonnwelt.ch</span>
      </div>
      <div class="contact__row">
        <svg class="contact__icon" viewBox="0 0 18 18" fill="none" stroke="var(--icon-orange)" stroke-width="1.4">
          <circle cx="9" cy="9" r="7.5"/><ellipse cx="9" cy="9" rx="3.2" ry="7.5"/>
          <line x1="1.5" y1="9" x2="16.5" y2="9"/><line x1="3" y1="5" x2="15" y2="5"/><line x1="3" y1="13" x2="15" y2="13"/>
        </svg>
        <span>www.lukasbrenner.coach</span>
      </div>
    </div>
  </section>

</body>
</html>
```